Vantrel Ashcombe LLC

we need a business card design

Industry/Entity Type

hvac

Contact Information for Business Card

my logo

Requirements
Must have
• my logo and same colors

```html
<!DOCTYPE html>
<html lang="en">
<head>
<meta charset="utf-8">
<title>Vantrel Ashcombe LLC – Business Card</title>
<link rel="stylesheet" href="https://fonts.googleapis.com/css2?family=Montserrat:wght@400;500;700;800&display=swap">
<style>
  :root {
    --brand-blue: #1160ab;
    --brand-blue-deep: #0d4f94;
    --sky-blue: #1fa3e0;
    --accent-gold: #f2b73f;
    --ink: #2b2b2b;
    --paper: #ffffff;
    --stage: #2a2a2a;
  }
  * { box-sizing: border-box; margin: 0; padding: 0; }
  html, body { width: 1200px; height: 900px; overflow: hidden; }
  body {
    background: var(--stage);
    font-family: "Montserrat", Arial, sans-serif;
    position: relative;
  }
  .card {
    position: absolute;
    width: 660px;
    height: 377px;
    border-radius: 22px;
    overflow: hidden;
    box-shadow: 0 18px 40px rgba(0,0,0,0.45);
  }
  .card-back {
    left: 110px;
    top: 50px;
    background: var(--brand-blue);
    display: flex;
    align-items: center;
    justify-content: center;
  }
  .card-front {
    left: 430px;
    top: 470px;
    background: var(--paper);
  }
  .brand-name {
    font-weight: 800;
    text-transform: uppercase;
    line-height: 1.1;
    text-align: center;
    letter-spacing: 1px;
  }
  .card-back .brand-name {
    color: var(--paper);
    font-size: 40px;
  }
  .card-front .brand-name {
    position: absolute;
    left: 30px;
    top: 120px;
    width: 270px;
    color: var(--brand-blue);
    font-size: 28px;
  }
  .divider {
    position: absolute;
    left: 318px;
    top: 60px;
    width: 2px;
    height: 200px;
    background: var(--accent-gold);
  }
  .contact {
    position: absolute;
    left: 345px;
    top: 58px;
    color: var(--ink);
  }
  .contact-name {
    color: var(--brand-blue);
    font-weight: 800;
    font-size: 26px;
    letter-spacing: 0.5px;
  }
  .contact-role {
    font-size: 15px;
    margin-top: 2px;
  }
  .contact-address {
    font-size: 15px;
    line-height: 1.4;
    margin-top: 16px;
  }
  .contact-lines {
    list-style: none;
    margin-top: 14px;
    font-size: 15px;
    line-height: 1.7;
  }
  .contact-lines li { display: flex; align-items: center; gap: 8px; }
  .contact-lines svg { width: 14px; height: 14px; fill: var(--brand-blue); }
  .swoosh {
    position: absolute;
    left: 0;
    bottom: 0;
    width: 660px;
    height: 170px;
  }
  .website {
    position: absolute;
    right: 28px;
    bottom: 26px;
    color: var(--paper);
    font-size: 15px;
    font-weight: 500;
    letter-spacing: 0.5px;
  }
</style>
</head>
<body>
  <section class="card card-back" aria-label="Card back">
    <p class="brand-name">Vantrel<br>Ashcombe LLC</p>
  </section>

  <section class="card card-front" aria-label="Card front">
    <p class="brand-name">Vantrel<br>Ashcombe LLC</p>
    <div class="divider"></div>

    <div class="contact">
      <h1 class="contact-name">DORIAN KELLWAY</h1>
      <p class="contact-role">Founder</p>
      <p class="contact-address">4/22 Harlow Ridge Rd<br>Merrivale ABC 5132</p>
      <ul class="contact-lines">
        <li>
          <svg viewBox="0 0 24 24" aria-hidden="true"><path d="M6.6 10.8a15.1 15.1 0 0 0 6.6 6.6l2.2-2.2a1 1 0 0 1 1-.25 11.4 11.4 0 0 0 3.6.57 1 1 0 0 1 1 1V20a1 1 0 0 1-1 1A17 17 0 0 1 3 4a1 1 0 0 1 1-1h3.5a1 1 0 0 1 1 1c0 1.25.2 2.45.57 3.57a1 1 0 0 1-.25 1z"/></svg>
          303.555.0147
        </li>
        <li>
          <svg viewBox="0 0 24 24" aria-hidden="true"><path d="M2 5h20v14H2z M2 5l10 8 10-8" fill="none" stroke="#1160ab" stroke-width="2"/></svg>
          info@vantrelashcombe.com
        </li>
      </ul>
    </div>

    <svg class="swoosh" viewBox="0 0 660 170" preserveAspectRatio="none" aria-hidden="true">
      <path d="M200 170 C 330 80, 480 40, 660 20 L 660 170 Z" fill="var(--sky-blue)"/>
      <path d="M225 170 C 350 95, 490 60, 660 40 L 660 170 Z" fill="var(--paper)"/>
      <path d="M240 170 C 360 100, 500 70, 660 48 L 660 170 Z" fill="var(--brand-blue)"/>
    </svg>
    <p class="website">www.vantrelashcombe.com</p>
  </section>
</body>
</html>
```